M.A.P.L.E.S. Infographic

I need I do need an infographic based on the 6 elements of my curriculum using the imagery of a path with a sunrise at the end.
The attached is a poor rendering with lots of mistakes and missing info but you can use this as a starting point. Here is a description of what I need:
Headline:
Shaping Bright Days Amid Quiet Ears: M.A.P.L.E.S.
6 Elements of the M.A.P.L.E.S. curriculum:
Learn to Adapt to Hearing Loss - with the proper use of the right technology and communication strategies
Interact with Purpose – for more fulfilling relationships
Sustain Vitality – with effective habits for mental and physical health
Embrace Growth – to enjoy the benefits of lifelong learning
Nurture Motivation – to continue progressing
Use the following brand colors and fonts:
Hex colors:
#65A4DB Blue
#F1DC75 Yellow
#DB9C65 Sienna
#AAB47A Green
Fonts:
Open Sans font for (headlines)
Lora Google font for (subhead and text)

```html
<!DOCTYPE html>
<html lang="en">
<head>
<meta charset="utf-8">
<title>Shaping Bright Days Amid Quiet Ears: M.A.P.L.E.S.</title>
<link rel="stylesheet" href="https://fonts.googleapis.com/css2?family=Open+Sans:wght@300;400;700;800&family=Lora:wght@400&display=swap">
<style>
  :root {
    --blue: #65a4db;
    --blue-deep: #2a7fc0;
    --teal: #44a9c3;
    --sienna: #db9c65;
    --yellow: #f1dc75;
    --yellow-soft: #f6ec9c;
    --green: #8a8e70;
    --navy: #2b2a63;
    --slate: #2d5b70;
    --ink: #222222;
    --paper: #ffffff;
  }
  * { margin: 0; padding: 0; box-sizing: border-box; }
  html, body { width: 776px; height: 1200px; overflow: hidden; background: var(--paper); }
  .infographic { position: relative; width: 776px; height: 1200px; overflow: hidden; background: var(--paper); }

  .masthead {
    position: absolute; left: 0; top: 0; width: 776px; height: 200px;
    background: var(--blue); color: var(--paper);
    font-family: "Open Sans", sans-serif; font-weight: 700; text-align: center;
  }
  .masthead__line1 { position: absolute; left: 0; right: 0; top: 50px; font-size: 46px; line-height: 1; letter-spacing: 0.5px; }
  .masthead__line1 small { font-size: 33px; }
  .masthead__line2 { position: absolute; left: 0; right: 0; top: 96px; font-size: 84px; line-height: 1; letter-spacing: 1px; }

  .rule-band { position: absolute; left: 0; top: 216px; width: 776px; height: 18px; }
  .kicker {
    position: absolute; left: 0; right: 0; top: 210px; text-align: center;
    font-family: "Open Sans", sans-serif; font-weight: 400; font-size: 27px; color: var(--slate);
  }
  .kicker span { background: var(--paper); padding: 0 6px; }
  .kicker-sub {
    position: absolute; left: 0; right: 0; top: 248px; text-align: center;
    font-family: "Open Sans", sans-serif; font-weight: 700; font-size: 27px; color: var(--blue-deep); letter-spacing: 0.8px;
  }

  .path-lines { position: absolute; left: 0; top: 0; width: 776px; height: 1200px; }

  .element { position: absolute; }
  .element__title {
    font-family: "Open Sans", sans-serif; font-weight: 800; color: var(--navy);
    font-size: 27px; line-height: 1.02; letter-spacing: 0.3px;
  }
  .element__title--large { font-size: 50px; letter-spacing: 1px; }
  .element__text {
    font-family: "Lora", serif; font-size: 19px; line-height: 24px; color: var(--ink);
    text-transform: uppercase; letter-spacing: 0.2px;
  }

  .adapt { left: 150px; top: 332px; }
  .adapt .element__text { margin: 44px 0 0 5px; }
  .interact { left: 240px; top: 624px; }
  .interact .element__text { margin-top: 8px; }
  .vitality { left: 517px; top: 782px; width: 260px; }
  .vitality .element__text { width: 230px; margin: 14px 0 0 13px; text-align: center; }
  .growth { left: 47px; top: 828px; width: 280px; }
  .growth .element__text { width: 250px; text-align: center; margin-top: 12px; }
  .motivation { left: 172px; top: 1040px; }
  .motivation .element__text { margin: 10px 0 0 24px; }

  .art { position: absolute; }
  .art--ear { left: 515px; top: 330px; width: 165px; height: 255px; border-radius: 50% 50% 45% 55% / 40% 40% 60% 60%; background: linear-gradient(160deg, var(--yellow-soft), var(--yellow)); }
  .art--conversation { left: 45px; top: 612px; width: 180px; height: 145px; border-radius: 14px; background: linear-gradient(135deg, #d4ecf2, #f1dcc7); }
  .art--pair { left: 600px; top: 662px; width: 100px; height: 100px; border-radius: 12px; background: linear-gradient(135deg, #b9cbd3, #c7c9b6); }
  .art--network { left: 325px; top: 800px; width: 165px; height: 172px; border-radius: 50%; background: radial-gradient(circle, #efcfb2 0%, #cfe8ef 70%); }
  .art--sunrise {
    left: 520px; top: 975px; width: 190px; height: 215px; border-radius: 50% 50% 16px 16px;
    background: radial-gradient(circle at 50% 78%, #fff6c9 0%, var(--yellow) 30%, var(--sienna) 62%, #9cc8e8 100%);
  }

  .footer-band { position: absolute; left: 0; bottom: 0; width: 776px; height: 14px; background: var(--green); }
</style>
</head>
<body>
<main class="infographic">
  <header class="masthead">
    <h1>
      <span class="masthead__line1">SHAPING BRIGHT DAYS <small>AMID</small></span>
      <span class="masthead__line2">QUIET EARS</span>
    </h1>
  </header>

  <svg class="rule-band" viewBox="0 0 776 18" aria-hidden="true">
    <g fill="var(--slate)">
      <rect x="0" y="2" width="776" height="3"/>
      <rect x="0" y="8" width="776" height="3"/>
      <rect x="0" y="14" width="776" height="3"/>
    </g>
  </svg>
  <p class="kicker"><span>6 ELEMENTS OF THE</span></p>
  <p class="kicker-sub">M.A.P.L.E.S. CURRICULUM</p>

  <svg class="path-lines" viewBox="0 0 776 1200" aria-hidden="true" fill="none" stroke-width="7" stroke-linecap="round">
    <path stroke="var(--teal)" d="M525 414 L200 414 C140 414 110 455 112 500 C114 540 130 562 148 578"/>
    <path stroke="var(--sienna)" d="M55 600 C80 588 110 582 150 582 L420 582 C470 582 500 622 500 672 C500 712 485 735 470 745"/>
    <path stroke="var(--yellow-soft)" d="M40 785 C70 770 100 766 130 766 L420 766 C470 766 495 806 495 850 C495 890 480 915 465 928"/>
    <path stroke="var(--green)" d="M776 622 L640 622 C590 622 555 658 555 705 C555 732 565 752 575 765"/>
    <path stroke="var(--teal)" d="M560 1000 L230 1000 C160 1000 118 1042 118 1090 C118 1120 130 1142 145 1155"/>
  </svg>

  <div class="art art--ear" role="img" aria-label="Illustration of a human ear"></div>
  <div class="art art--conversation" role="img" aria-label="Icon of three people connected by a speech bubble and arrows"></div>
  <div class="art art--pair" role="img" aria-label="Icon of two people standing together"></div>
  <div class="art art--network" role="img" aria-label="Icon of a person at the centre of a connected network"></div>
  <div class="art art--sunrise" role="img" aria-label="Sunrise glowing on the horizon at the end of the path"></div>

  <section class="element adapt">
    <h2 class="element__title">LEARN TO ADAPT TO<br><span class="element__title--large">HEARING LOSS</span></h2>
    <p class="element__text">With the proper use of<br>the right technology<br>and communication<br>strategies</p>
  </section>

  <section class="element interact">
    <h2 class="element__title">INTERACT<br>WITH PURPOSE</h2>
    <p class="element__text">For more fulfilling<br>relationships</p>
  </section>

  <section class="element vitality">
    <h2 class="element__title">SUSTAIN VITALITY</h2>
    <p class="element__text">With effective<br>habits for<br>mental<br>and<br>physical health</p>
  </section>

  <section class="element growth">
    <h2 class="element__title">EMBRACE GROWTH</h2>
    <p class="element__text">To enjoy the benefits<br>of<br>lifelong learning</p>
  </section>

  <section class="element motivation">
    <h2 class="element__title">NURTURE MOTIVATION</h2>
    <p class="element__text">To continue progressing</p>
  </section>

  <div class="footer-band"></div>
</main>
</body>
</html>
```